Flyer PRTW

Everyone deserves true happiness.
Real Food is the answer to:
A body you love
Reverting illnesses
Healthy digestion
Stable blood sugar
Emotions in control
Blasting energy
Sound sleep
REAL food + water + exercise + Laughter =
“HIGH QUALITY OF LIFE “
EASY, right?
Challenging: certainly
Changing habits: reluctance in sight!
WE’RE OFFER TO:
1. Study YOUR unique body composition, food cravings, blockages, illnesses, and personality!
2. Introduce you to new Food
3. customized wellness plan with follow ups
4. meditation,cooking, and fitness classes as well as wellness workshops
5. New friends with high aspirations
LOGO
Contact info
Please visit our web address to see our design style and colors: www.pinerivertallwave.net
Target Market(s)
people who want to be more healthy
Industry/Entity Type
Fitness
Requirements
Must have
- beautiful pictures of fresh food (main picture) and maybe a few more small pictures reflecting
exercise
healthy living
meditation
Nice to have
- look is crucial. recall some of the color or colors from my logo to have a theme

```html
<!DOCTYPE html>
<html lang="en">
<head>
<meta charset="utf-8">
<title>PRTW Wellness Flyer</title>
<link href="https://fonts.googleapis.com/css2?family=Open+Sans:wght@400;600;700;800&family=Parisienne&display=swap" rel="stylesheet">
<style>
:root{
  --green:#8cc63f;
  --green-dark:#5f9a1e;
  --green-deep:#4d7f16;
  --green-pale:#e4f1c9;
  --green-soft:#d3e9a7;
  --green-ring:#a6d65f;
  --orange:#f39a1e;
  --orange-red:#f26b21;
  --gold:#f2a900;
  --white:#ffffff;
  --ink:#222222;
  --bg:#e9ebe8;
}
*{box-sizing:border-box;margin:0;padding:0}
html,body{width:1200px;height:900px;overflow:hidden;background:var(--bg);font-family:"Open Sans",Arial,sans-serif;color:var(--ink)}
.canvas{position:relative;width:1200px;height:900px}

/* Cover panel */
.cover{position:absolute;left:60px;top:60px;width:340px;height:780px;background:var(--white);overflow:hidden;box-shadow:0 2px 8px rgba(0,0,0,.15)}
.cover-photo{position:absolute;left:0;top:0;width:340px;height:265px;background:linear-gradient(135deg,#c9361f 0%,#7fae3a 40%,#e8d23a 70%,#6b4a2a 100%)}
.brand{position:absolute;left:22px;top:285px;display:flex;align-items:center;gap:12px}
.brand-dot{width:58px;height:58px;border-radius:50%;background:var(--green)}
.brand-name{font-size:27px;font-weight:700;color:var(--green-dark);line-height:1}
.brand-tag{position:absolute;left:92px;top:352px;font-size:8.5px;letter-spacing:.8px;font-weight:600;color:var(--green-deep)}
.cover-green{position:absolute;left:0;top:390px;width:340px;height:360px}
.cover-photo-round{position:absolute;border-radius:50%;border:4px solid var(--white)}
.round-1{left:20px;top:440px;width:120px;height:120px;background:linear-gradient(160deg,#9fcf5a,#c8392d 60%,#6a9a2e)}
.round-2{left:200px;top:430px;width:120px;height:120px;background:linear-gradient(160deg,#2f4a2a,#c8d7a0 55%,#3d5a30)}
.round-3{left:115px;top:560px;width:120px;height:120px;background:linear-gradient(160deg,#9bbf60,#7aa03c 50%,#d9b79a)}
.cover-slogan{position:absolute;left:18px;top:672px;font-family:"Parisienne",cursive;color:var(--white);font-size:31px;line-height:1.05}
.cover-slogan span{display:block;padding-left:80px}
.cover-foot{position:absolute;left:0;bottom:0;width:340px;height:30px;background:var(--green-pale);text-align:center;font-size:11px;font-weight:700;line-height:30px;color:var(--green-deep)}

/* Inside spread */
.spread{position:absolute;left:440px;top:60px;width:700px;height:780px;background:var(--white);overflow:hidden;box-shadow:0 2px 8px rgba(0,0,0,.15)}
.spread-head{position:absolute;left:0;top:0;width:700px;height:200px}
.head-text{position:absolute;left:0;top:12px;width:700px;text-align:center;color:var(--white)}
.head-line-1{font-size:14.5px;font-weight:700}
.head-line-2{font-size:17px;font-weight:700;margin-top:10px}
.head-line-3{font-size:15.5px;font-weight:800;margin-top:2px}
.head-line-4{font-size:15.5px;font-weight:700;color:var(--orange-red);margin-top:6px}
.fold{position:absolute;left:350px;top:200px;width:1px;height:550px;background:rgba(0,0,0,.08)}

.invest{position:absolute;left:0;top:190px;width:350px;height:560px}
.invest-title{text-align:center;font-size:22px;font-weight:800;color:var(--gold);margin-top:10px}
.invest-sub{text-align:center;font-size:11px;font-weight:700;line-height:1.35;margin-top:4px}
.mode{position:absolute;width:112px;height:112px;border-radius:50%;background:var(--green-pale);display:flex;align-items:center;justify-content:center;text-align:center;font-size:13px;font-weight:700;color:var(--green-dark);line-height:1.25}
.mode-video{left:18px;top:90px}
.mode-phone{left:220px;top:90px}
.mode-walk{left:18px;top:430px}
.mode-face{left:220px;top:430px}
.arrows-art{position:absolute;left:75px;top:210px;width:200px;height:210px;border-radius:20px;background:linear-gradient(135deg,#f39a1e 0%,#8cc63f 35%,#2aa3dd 65%,#e03a2a 100%);opacity:.85}

.includes{position:absolute;left:350px;top:190px;width:350px;height:560px}
.includes-title{text-align:center;font-size:22px;font-weight:800;color:var(--gold);line-height:1.15;margin-top:14px}
.include-list{list-style:none;margin:10px 18px 0;text-align:center;font-size:11.5px;line-height:1.5}
.include-list li::before{content:"";display:inline-block;width:6px;height:6px;border-radius:50%;background:var(--green);margin-right:5px;vertical-align:middle}
.plans{margin:12px 0 0;background:var(--green-soft);padding:9px 24px;list-style:none}
.plans li{font-size:13.5px;font-weight:700;color:var(--green-deep);line-height:1.6}
.plans li::before{content:"+";color:var(--orange);font-weight:800;font-size:16px;margin-right:8px}
.plans small{font-size:9px}
.policy{margin:14px 24px 0;font-size:10px;line-height:1.45;text-align:center}
.spread-foot{position:absolute;left:0;bottom:0;width:700px;height:30px;background:var(--green);text-align:center;color:var(--white);font-size:11px;font-weight:700;line-height:30px}
</style>
</head>
<body>
<main class="canvas">

  <section class="cover">
    <div class="cover-photo" role="img" aria-label="Photograph of fresh tomatoes, yellow peppers and lettuce in wooden bowls"></div>
    <div class="brand">
      <span class="brand-dot"></span>
      <span class="brand-name">Pinerivertallwave</span>
    </div>
    <p class="brand-tag">BALANCED NUTRITION, MIND, AND FITNESS</p>
    <svg class="cover-green" viewBox="0 0 340 360" preserveAspectRatio="none" aria-hidden="true">
      <path d="M0 30 Q170 -10 340 20 L340 360 L0 360 Z" fill="#8cc63f"/>
      <circle cx="300" cy="120" r="40" fill="none" stroke="#a6d65f" stroke-width="14"/>
      <circle cx="40" cy="300" r="28" fill="none" stroke="#a6d65f" stroke-width="10"/>
    </svg>
    <div class="cover-photo-round round-1" role="img" aria-label="Photograph of a woman stretching on the grass in a park"></div>
    <div class="cover-photo-round round-2" role="img" aria-label="Photograph of a woman meditating in sunlight"></div>
    <div class="cover-photo-round round-3" role="img" aria-label="Photograph of a woman and man exercising outdoors"></div>
    <p class="cover-slogan">Everyone deserves<span>true happiness</span></p>
    <footer class="cover-foot">www.pinerivertallwave.net</footer>
  </section>

  <section class="spread">
    <svg class="spread-head" viewBox="0 0 700 200" preserveAspectRatio="none" aria-hidden="true">
      <path d="M0 0 H700 V175 Q520 140 350 190 Q170 235 0 165 Z" fill="#8cc63f"/>
      <path d="M0 165 Q170 235 350 190 Q520 140 700 175 V185 Q520 152 350 200 Q170 245 0 175 Z" fill="#d3e9a7"/>
    </svg>
    <div class="head-text">
      <p class="head-line-1">Wellness coaching program – Invest in 6 months of coaching for LIFELONG BENEFITS</p>
      <p class="head-line-2">Work with our Food &amp; wellness coach in the areas of:</p>
      <p class="head-line-3">NUTRITION - WELL BEING – STRESS – SLEEP - AND WEIGHT MANAGEMENT.</p>
      <p class="head-line-4">Our sessions can be conducted in whichever way is more convenient for you!</p>
    </div>
    <div class="fold"></div>

    <div class="invest">
      <h2 class="invest-title">INVEST IN YOUR LIFE!</h2>
      <p class="invest-sub">Achieve the life you always wanted.<br>Feel energized, alive, and love yourself.</p>
      <div class="mode mode-video">Throught<br>Video<br>Conferencing</div>
      <div class="mode mode-phone">Over<br>the<br>Telephone</div>
      <div class="arrows-art" role="img" aria-label="Illustration of four curved 3D arrows in orange, green, blue and red pointing to the four session options"></div>
      <div class="mode mode-walk">While<br>Walking<br>Together</div>
      <div class="mode mode-face">Face to Face<br>- in my office<br>- over a cup<br>of coffee</div>
    </div>

    <div class="includes">
      <h2 class="includes-title">Wellness Coaching<br>Program Includes:</h2>
      <ul class="include-list">
        <li>FREE initial Health History Consultation by phone (EXCEPT for 1 month program)</li>
        <li>Bi-monthly, 50 to 60 -minute private sessions</li>
        <li>Complete access to membership Zone with Health and cooking videos</li>
        <li>Detailed recommendations at each sessions</li>
        <li>Free goodies and food sampling</li>
        <li>Action planning and goal setting</li>
        <li>Stress management and relaxation tools</li>
        <li>Weekly diet journal feedback</li>
        <li>Unlimited E-mail support between sessions</li>
        <li>Handouts and other informational materials</li>
        <li>Access to a variety of recipes and cooking techniques</li>
      </ul>
      <ul class="plans">
        <li>6 Months of Wellness Coaching <small>(Most Popular)</small></li>
        <li>3 Months of Wellness Coaching</li>
        <li>1 Month of Wellness Coaching</li>
      </ul>
      <p class="policy">PRTW wellness coaches work on a scheduled appointment basis. Because your appointment time has been reserved especially for you, we require 24-hours notice when canceling an appointment. Given proper notice, you are free to reschedule with no charge. Appointments canceled with less than 24-hours notice are charged at the full non-refundable price.</p>
    </div>

    <footer class="spread-foot">www.pinerivertallwave.net</footer>
  </section>

</main>
</body>
</html>
```